Flyer für Handwerksunternehmen
Zielgruppe
Wir sind ein Handwerksunternehmen. Wir bieten alle Leistungen aus einer Hand. Mehr Infos unter www.werkbaukolleg.de
Aufgabenstellung
Modernes Design

```html
<!DOCTYPE html>
<html lang="de">
<head>
<meta charset="utf-8">
<title>Werkbaukolleg – Baumanagement Flyer</title>
<link rel="stylesheet" href="https://fonts.googleapis.com/css2?family=Raleway:wght@400;500;800&display=swap">
<style>
  :root {
    --bg: #1f1b1b;
    --band: #3a3838;
    --band-edge: #2c2a2a;
    --brand-grey: #3d3c40;
    --sub-grey: #8c8c8e;
    --white: #ffffff;
    --box-green: #2b5a22;
    --green-dark: #0e5a2c;
    --green-mid: #4f8a35;
    --green-light: #9bb55a;
  }
  html, body {
    margin: 0;
    padding: 0;
    overflow: hidden;
    background: var(--bg);
  }
  .flyer {
    position: relative;
    width: 928px;
    height: 1200px;
    overflow: hidden;
    background: var(--bg);
    font-family: "Raleway", sans-serif;
    color: var(--white);
  }
  .texture-band {
    position: absolute;
    inset: 0;
  }
  .brand {
    position: absolute;
    left: 135px;
    top: 46px;
    width: 658px;
    text-align: center;
    color: var(--brand-grey);
    font-weight: 800;
  }
  .brand-name {
    font-size: 56px;
    line-height: 1;
    letter-spacing: 0.5px;
  }
  .brand-sub {
    margin-top: 14px;
    font-size: 30px;
    letter-spacing: 26px;
    margin-right: -26px;
    line-height: 1;
  }
  .headline {
    position: absolute;
    left: 20px;
    top: 282px;
    width: 432px;
    margin: 0;
    text-align: center;
    font-weight: 400;
    font-size: 40px;
    line-height: 51px;
  }
  .building-graphic {
    position: absolute;
    left: 379px;
    top: 158px;
    width: 502px;
    height: 422px;
  }
  .question {
    position: absolute;
    left: 150px;
    top: 598px;
    width: 628px;
    margin: 0;
    text-align: center;
    font-weight: 400;
    font-size: 31px;
    line-height: 41px;
  }
  .contact {
    position: absolute;
    left: 50px;
    display: flex;
    align-items: center;
    background: var(--box-green);
    height: 64px;
    box-sizing: border-box;
    color: var(--white);
    font-weight: 400;
  }
  .contact svg { flex: none; }
  .contact-phone { top: 866px; width: 329px; padding-left: 4px; font-size: 30px; }
  .contact-mail { top: 956px; width: 510px; padding-left: 4px; font-size: 24px; }
  .contact-address { top: 1049px; width: 510px; padding-left: 8px; font-size: 24px; }
  .contact-phone span { margin-left: 4px; }
  .contact-mail span { margin-left: 14px; }
  .contact-address span { margin-left: 38px; }
</style>
</head>
<body>
<div class="flyer">
  <svg class="texture-band" width="928" height="1200" viewBox="0 0 928 1200" role="img" aria-label="Diagonales Band mit dunkler Betonstruktur">
    <defs>
      <linearGradient id="bandFill" x1="0" y1="0" x2="1" y2="1">
        <stop offset="0" stop-color="#454343"/>
        <stop offset="0.5" stop-color="#3a3838"/>
        <stop offset="1" stop-color="#302e2e"/>
      </linearGradient>
    </defs>
    <polygon points="0,30 20,0 150,0 928,1100 928,1200 870,1200 0,140" fill="url(#bandFill)"/>
  </svg>

  <div class="brand">
    <div class="brand-name">WERKBAUKOLLEG</div>
    <div class="brand-sub">BAUMANAGEMENT</div>
  </div>

  <h1 class="headline">BAUMANAGEMENT<br>MIT LANGJÄHRIGER<br>ERFAHRUNG</h1>

  <svg class="building-graphic" viewBox="0 0 502 422" role="img" aria-label="Grüne Gebäudegrafik">
    <defs>
      <linearGradient id="greenFill" x1="0.2" y1="0" x2="0.4" y2="1">
        <stop offset="0" stop-color="#0e5a2c"/>
        <stop offset="0.55" stop-color="#4f8a35"/>
        <stop offset="1" stop-color="#9bb55a"/>
      </linearGradient>
    </defs>
    <polygon points="301,0 502,200 502,422 55,422 0,260" fill="url(#greenFill)" opacity="0.85"/>
  </svg>

  <p class="question">BENÖTIGEN SIE FÜR IHR PROJEKT<br>EINE ERSTKLASSIGE<br>DIENSTLEISTUNG, DIE IHREN<br>ANSPRÜCHEN GERECHT WIRD UND<br>DENNOCH PREISWERT IST?</p>

  <div class="contact contact-phone">
    <svg width="52" height="52" viewBox="0 0 52 52" fill="none" stroke="#fff" stroke-width="2.2" stroke-linecap="round" stroke-linejoin="round" aria-hidden="true">
      <path d="M14 8l7 9-4 5c2 5 6 9 11 12l5-4 9 7-4 6c-10 1-27-15-28-28z"/>
      <path d="M30 12a10 10 0 0 1 10 10"/>
      <path d="M30 5a17 17 0 0 1 17 17"/>
    </svg>
    <span>06221-4870300</span>
  </div>

  <div class="contact contact-mail">
    <svg width="52" height="52" viewBox="0 0 52 52" fill="none" stroke="#fff" stroke-width="2" stroke-linejoin="round" aria-hidden="true">
      <path d="M3 22l23-16 23 16v24H3z"/>
      <path d="M3 22l23 15 23-15"/>
      <path d="M3 46l17-13M49 46l-17-13"/>
      <path d="M13 26V13h26v13M19 18h14M19 22h14"/>
    </svg>
    <span>KONTAKT@WERKBAUKOLLEG.DE</span>
  </div>

  <div class="contact contact-address">
    <svg width="34" height="52" viewBox="0 0 34 52" fill="none" stroke="#fff" stroke-width="2.2" aria-hidden="true">
      <path d="M17 3a14 14 0 0 0-14 14c0 11 14 27 14 27s14-16 14-27A14 14 0 0 0 17 3z"/>
      <circle cx="17" cy="17" r="6"/>
      <ellipse cx="17" cy="46" rx="8" ry="3"/>
    </svg>
    <span>Am Lindenhang 12, Nussloch 69226</span>
  </div>
</div>
</body>
</html>
```